Medical Oncologist in Rural Australia needs a Business Card

I am a medical oncologist in a regional town in Australia. I need a business card that merges a degree of conservatism (as people's lives are entrusted to me) with cutting edge (as I am always trying to understand the latest cancer biology and trying to bring new drugs to patients rapidly). I wish my card to project the idea that I am trustworthy, caring and innovative. Not overly bold colours but something that doesn't drift into the background.

Industry/Entity Type

Medical

```html
<!DOCTYPE html>
<html lang="en">
<head>
<meta charset="utf-8">
<title>Dr. Adam Kessler – Business Card</title>
<link href="https://fonts.googleapis.com/css2?family=Michroma&family=Dosis:wght@400;500&display=swap" rel="stylesheet">
<style>
  :root {
    --brand-blue: #3aacdc;
    --ink: #333a40;
    --ink-soft: #4a4f55;
    --paper: #ffffff;
    --backdrop: #ffffff;
    --mark-tone: #8fa9c9;
  }
  * { box-sizing: border-box; margin: 0; padding: 0; }
  html, body { width: 1200px; height: 1000px; overflow: hidden; background: var(--backdrop); }
  .canvas { position: relative; width: 1200px; height: 1000px; }

  .card {
    position: absolute;
    width: 472px; height: 284px;
    background: var(--paper);
    box-shadow: 0 1px 4px rgba(0,0,0,0.28);
    overflow: hidden;
  }
  .card--front { left: 84px; top: 80px; }
  .card--back  { left: 640px; top: 80px; }

  /* Front */
  .identity { position: absolute; left: 26px; top: 68px; }
  .identity__name {
    font-family: "Michroma", sans-serif;
    font-size: 13px; letter-spacing: 1.6px;
    color: var(--ink);
  }
  .identity__credentials {
    font-family: "Dosis", sans-serif;
    font-size: 13px; color: var(--ink-soft);
    margin-top: 5px;
  }
  .identity__practice {
    font-family: "Michroma", sans-serif;
    font-size: 9.5px; letter-spacing: 0.9px;
    color: var(--brand-blue);
    margin-top: 16px;
  }
  .identity__address {
    font-family: "Dosis", sans-serif;
    font-size: 13px; color: var(--ink-soft);
    margin-top: 6px;
  }
  .identity__email {
    display: flex; align-items: center; gap: 4px;
    font-family: "Dosis", sans-serif;
    font-size: 13px; color: var(--ink-soft);
    margin-top: 12px;
  }

  .practice-mark {
    position: absolute;
    display: flex; align-items: center; gap: 7px;
    font-family: "Dosis", sans-serif; font-weight: 500;
    color: var(--mark-tone);
  }
  .practice-mark__dot { border-radius: 50%; background: var(--mark-tone); flex: none; }
  .card--front .practice-mark { left: 292px; top: 86px; width: 160px; font-size: 14px; line-height: 1.15; }
  .card--front .practice-mark__dot { width: 14px; height: 14px; }

  .contact-band {
    position: absolute; left: 0; bottom: 0;
    width: 100%; height: 74px;
    background: var(--brand-blue);
    display: flex; gap: 20px;
    padding: 20px 0 0 26px;
  }
  .contact-group__label {
    font-family: "Michroma", sans-serif;
    font-size: 8.5px; letter-spacing: 0.6px;
    color: var(--ink);
  }
  .contact-group__lines { display: flex; gap: 12px; margin-top: 9px; }
  .contact-line {
    display: flex; align-items: center; gap: 5px;
    font-family: "Dosis", sans-serif; font-size: 13px;
    color: var(--ink);
  }
  .icon { width: 12px; height: 12px; fill: var(--paper); flex: none; }

  /* Back */
  .name-band {
    position: absolute; left: 0; top: 0;
    width: 98px; height: 100%;
    background: var(--brand-blue);
    display: flex; justify-content: center; gap: 8px;
    padding-top: 16px;
  }
  .name-band__text {
    writing-mode: vertical-rl;
    transform: rotate(180deg);
    white-space: nowrap;
    font-family: "Michroma", sans-serif;
  }
  .name-band__name { font-size: 17px; letter-spacing: 2.4px; color: var(--paper); }
  .name-band__practice { font-size: 10px; letter-spacing: 1.2px; color: var(--ink); }

  .card--back .practice-mark { left: 150px; top: 118px; font-size: 22px; }
  .card--back .practice-mark__dot { width: 26px; height: 26px; }
</style>
</head>
<body>
<main class="canvas">

  <section class="card card--front" aria-label="Business card front">
    <div class="identity">
      <h1 class="identity__name">DR. ADAM KESSLER</h1>
      <p class="identity__credentials">MBBS FRACP (Hons) BE (Hons)</p>
      <p class="identity__practice">TABLELANDS MEDICAL ONCOLOGY</p>
      <p class="identity__address">48 Hartley St, Millbrook, NSW 2799</p>
      <p class="identity__email">
        <svg class="icon" viewBox="0 0 12 12" style="fill:none;stroke:var(--brand-blue);stroke-width:1.6"><circle cx="6" cy="6" r="2"/><path d="M8 6v1.2a1.6 1.6 0 0 0 3.2 0V6A5.2 5.2 0 1 0 8.5 10.6"/></svg>
        adam.kessler@tableland.edu.au
      </p>
    </div>

    <div class="practice-mark" aria-label="Practice name">
      <span class="practice-mark__dot"></span>
      <span>Tablelands Medical Oncology</span>
    </div>

    <div class="contact-band">
      <div class="contact-group">
        <p class="contact-group__label">TABLELANDS MEDICAL ONCOLOGY</p>
        <div class="contact-group__lines">
          <span class="contact-line">
            <svg class="icon" viewBox="0 0 12 12"><path d="M2.6 0.8l2 2.3-1.1 1.5c.7 1.5 1.9 2.7 3.4 3.4l1.5-1.1 2.3 2-1.2 2.1C5.1 10.8 1.2 6.9 0.8 2z"/></svg>
            02 5550 4963
          </span>
          <span class="contact-line">
            <svg class="icon" viewBox="0 0 12 12"><rect x="2.5" y="0.8" width="7" height="4" rx="0.5"/><rect x="1" y="5.4" width="10" height="5.8" rx="1"/></svg>
            02 5550 8409
          </span>
        </div>
      </div>
      <div class="contact-group">
        <p class="contact-group__label">MILLBROOK HOSPITAL</p>
        <div class="contact-group__lines">
          <span class="contact-line">
            <svg class="icon" viewBox="0 0 12 12"><path d="M2.6 0.8l2 2.3-1.1 1.5c.7 1.5 1.9 2.7 3.4 3.4l1.5-1.1 2.3 2-1.2 2.1C5.1 10.8 1.2 6.9 0.8 2z"/></svg>
            02 5551 3380
          </span>
          <span class="contact-line">
            <svg class="icon" viewBox="0 0 12 12"><rect x="2.5" y="0.8" width="7" height="4" rx="0.5"/><rect x="1" y="5.4" width="10" height="5.8" rx="1"/></svg>
            02 5551 3868
          </span>
        </div>
      </div>
    </div>
  </section>

  <section class="card card--back" aria-label="Business card back">
    <div class="name-band">
      <span class="name-band__text name-band__name">DR. ADAM KESSLER</span>
      <span class="name-band__text name-band__practice">TABLELANDS MEDICAL ONCOLOGY</span>
    </div>
    <div class="practice-mark" aria-label="Practice name">
      <span class="practice-mark__dot"></span>
      <span>Tablelands Medical Oncology</span>
    </div>
  </section>

</main>
</body>
</html>
```